Our architectural studio needs a new business card

We need a business card design for our studio based in Waterloo in Belgium. We are active in architecture, design and installation.
Our works are contemporary and minimalist. our clients are refined and cultured.
Our business card must be minimalist and refined.

Reason: Some designers have accepted my invitation but they don't have all replied. I want to give them a chance to make one proposal. Paul

Target Market(s)

architecture

Industry/Entity Type

Business

Contact Information for Business Card

studio: paul dorsande studio
paul dorsande, architecte
M. +32 471 982 615
F. +322 618 4097
www.pauldorsande-example.com
paul@pauldorsande-example.com
14 rue des Margelles
2150 Valbrume
Belgium

Font styles to use
Sans Serif

Requirements
Must have
• simple, minimalist, clear, elegant and chic! Black and white
Nice to have
• embossed logo, other format like a square for example
Should not have
• color, fantasy, curves, ...

```html
<!DOCTYPE html>
<html lang="fr">
<head>
<meta charset="utf-8">
<title>paul dorsande studio – cartes de visite</title>
<link rel="stylesheet" href="https://fonts.googleapis.com/css2?family=Mulish:wght@400;700&family=Roboto+Slab:wght@800&display=swap">
<style>
  :root {
    --ink: #141414;
    --paper: #f1f0ec;
    --backdrop: #d9d9d7;
    --rule: #1c1c1c;
  }
  * { margin: 0; padding: 0; box-sizing: border-box; }
  html, body { width: 1200px; height: 900px; overflow: hidden; }
  body {
    background: var(--backdrop);
    font-family: "Mulish", sans-serif;
    color: var(--ink);
    position: relative;
  }
  .card {
    position: absolute;
    left: 280px;
    width: 640px;
    height: 370px;
    background: var(--paper);
  }
  .card--back { top: 60px; }
  .card--front { top: 470px; }

  .studio-name {
    display: flex;
    align-items: center;
    gap: 10px;
    font-family: "Mulish", sans-serif;
    font-weight: 700;
    text-transform: uppercase;
    letter-spacing: 0.22em;
    color: var(--ink);
    white-space: nowrap;
  }
  .studio-name__square {
    display: block;
    background: var(--ink);
    flex: none;
  }
  .card--back .studio-name {
    position: absolute;
    left: 50%;
    top: 50%;
    transform: translate(-50%, -50%);
    font-size: 16px;
  }
  .card--back .studio-name__square { width: 16px; height: 16px; }

  .person {
    position: absolute;
    left: 56px;
    top: 52px;
  }
  .person__name {
    font-family: "Roboto Slab", serif;
    font-weight: 800;
    font-size: 17px;
    line-height: 1.2;
  }
  .person__role {
    font-size: 15px;
    line-height: 1.3;
  }
  .rule {
    position: absolute;
    height: 1px;
    background: var(--rule);
  }
  .rule--main { left: 56px; right: 40px; top: 186px; }
  .rule--studio { left: 356px; right: 40px; top: 236px; }

  .contact {
    position: absolute;
    left: 56px;
    top: 206px;
    list-style: none;
    font-size: 15px;
    line-height: 1.45;
  }
  .contact__label {
    display: inline-block;
    width: 18px;
  }

  .card--front .studio-name {
    position: absolute;
    left: 356px;
    top: 208px;
    font-size: 11px;
  }
  .card--front .studio-name__square { width: 10px; height: 10px; }

  .address {
    position: absolute;
    left: 356px;
    top: 250px;
    font-style: normal;
    font-size: 15px;
    line-height: 1.45;
    white-space: nowrap;
  }
</style>
</head>
<body>
  <section class="card card--back" aria-label="Verso de la carte">
    <div class="studio-name"><span class="studio-name__square"></span>paul dorsande studio</div>
  </section>

  <section class="card card--front" aria-label="Recto de la carte">
    <div class="person">
      <p class="person__name">paul dorsande</p>
      <p class="person__role">architecte</p>
    </div>

    <div class="rule rule--main"></div>

    <ul class="contact">
      <li><span class="contact__label">M</span>+32 471 982 615</li>
      <li><span class="contact__label">F</span>+322 618 4097</li>
      <li><span class="contact__label">E</span>paul@pauldorsande-example.com</li>
    </ul>

    <div class="studio-name"><span class="studio-name__square"></span>paul dorsande studio</div>
    <div class="rule rule--studio"></div>

    <address class="address">
      14 rue des Margelles 2150<br>
      Valbrume Belgium<br>
      www.pauldorsande-example.com
    </address>
  </section>
</body>
</html>
```